Tullers Letterhead

I would like to create a letterhead file similar to what we have but in MS Word format. Right now this is a PDF and is not functional

```html
<!DOCTYPE html>
<html lang="en">
<head>
<meta charset="utf-8">
<title>Tullers Hockey Club Letterhead</title>
<link rel="stylesheet" href="https://fonts.googleapis.com/css2?family=Bebas+Neue&family=Poppins:wght@300;400&display=swap">
<style>
  :root {
    --navy: #05053a;
    --gold: #fdb71c;
    --paper: #ffffff;
    --backdrop: #e4e4e6;
  }
  * { margin: 0; padding: 0; box-sizing: border-box; }
  html, body { width: 1040px; height: 1200px; overflow: hidden; background: var(--backdrop); }
  .letterhead {
    position: absolute; left: 80px; top: 30px;
    width: 880px; height: 1139px;
    background: var(--paper);
    overflow: hidden;
    box-shadow: 0 6px 24px rgba(0,0,0,0.18);
  }
  .header-band {
    position: absolute; left: 0; top: 0; width: 100%; height: 165px;
    background: var(--navy);
  }
  .accent-bar-left {
    position: absolute; left: 26px; top: 0; width: 38px; height: 204px;
    background: var(--gold);
  }
  .club-mark {
    position: absolute; left: 81px; top: 64px; width: 118px;
    font-family: "Bebas Neue", sans-serif; font-size: 44px; line-height: 44px;
    color: var(--gold); text-align: center; letter-spacing: 1px;
  }
  .club-title {
    position: absolute; left: 217px; top: 56px;
    font-family: "Bebas Neue", sans-serif; font-size: 40px; line-height: 40px;
    color: #fff; letter-spacing: 0.2px;
  }
  .club-town {
    position: absolute; left: 217px; top: 99px;
    font-family: "Poppins", sans-serif; font-weight: 300; font-size: 19px; line-height: 24px;
    color: #fff; letter-spacing: 0.5px;
  }
  .contact-list {
    position: absolute; right: 53px; top: 50px; list-style: none;
    font-family: "Poppins", sans-serif; font-weight: 300; font-size: 14px; color: #fff;
  }
  .contact-item {
    display: flex; align-items: center; justify-content: flex-end;
    height: 25.5px; gap: 14px;
  }
  .contact-icon { width: 23px; height: 20px; fill: var(--gold); flex: none; }
  .footer-band {
    position: absolute; left: 0; bottom: 0; width: 100%; height: 34px;
    background: var(--navy);
  }
  .accent-bar-right {
    position: absolute; left: 815px; bottom: 0; width: 39px; height: 55px;
    background: var(--gold);
  }
</style>
</head>
<body>
  <main class="letterhead">
    <header class="header-band">
      <div class="club-mark">TULLERS</div>
      <h1 class="club-title">TULLERS HOCKEY CLUB</h1>
      <p class="club-town">BROOKVALE</p>
      <ul class="contact-list">
        <li class="contact-item">780-555-0142
          <svg class="contact-icon" viewBox="0 0 24 24" aria-hidden="true">
            <circle cx="12" cy="12" r="10.5" fill="none" stroke="var(--gold)" stroke-width="1.6"/>
            <path d="M8.6 6.5l1.8-.4 1.3 2.9-1.2 1c.6 1.4 1.6 2.5 3 3.2l1-1.2 2.9 1.3-.4 1.8c-.2.6-.8 1-1.5.9-4-.6-7-3.6-7.6-7.6-.1-.7.3-1.3.7-1.5z"/>
          </svg>
        </li>
        <li class="contact-item">48 Linden Road, Brookvale AB
          <svg class="contact-icon" viewBox="0 0 24 24" aria-hidden="true">
            <path d="M12 2L1 12h3.2v10h5.6v-6h4.4v6h5.6V12H23L19 8.4V3h-3v2.7z"/>
          </svg>
        </li>
        <li class="contact-item">brookvaletullers.ca
          <svg class="contact-icon" viewBox="0 0 24 24" aria-hidden="true">
            <path d="M1 4h22v16H1z M2.5 5.5l9.5 8 9.5-8" fill="none" stroke="var(--gold)" stroke-width="1.6"/>
            <path d="M1 4h22L12 13.2z"/>
          </svg>
        </li>
      </ul>
    </header>
    <div class="accent-bar-left"></div>
    <footer class="footer-band"></footer>
    <div class="accent-bar-right"></div>
  </main>
</body>
</html>
```